Kestrel Shore Camp

We need a web page that details location/distance to Melbourne, the facilities available, the magnificent setting, contact information, history of the area and our background in the industry booking enquiry page linked to our email account, feedback page.
(Refer www.campdunmorecove.com.au for details and further imagary as we operate in the same facility and Camp Dunmore Cove Business no longer exists) WE WANT A BETTER WEBSITE THAN THIS!!

```html
<!DOCTYPE html>
<html lang="en">
<head>
<meta charset="utf-8">
<title>Kestrel Shore Camp</title>
<link href="https://fonts.googleapis.com/css2?family=Arimo:wght@400;700&family=Noto+Sans:wght@400&display=swap" rel="stylesheet">
<style>
  :root{
    --bar-dark:#141518;
    --bar-mid:#2e3036;
    --sky-top:#4f6fe0;
    --sky-mid:#7d93e6;
    --sand:#c9c5cf;
    --panel:rgba(78,84,118,.84);
    --head:#2f3450;
    --head-light:#454b68;
    --touch:#3c3f52;
    --btn:#1f6fa0;
    --footer:#121524;
    --footer-box:#1b1f33;
    --footer-head:#8a91ab;
    --footer-link:#7d8296;
    --base:#000;
    --white:#ffffff;
    --orange:#f07c1c;
  }
  *{margin:0;padding:0;box-sizing:border-box}
  html,body{width:1049px;height:1200px;overflow:hidden;background:var(--base)}
  body{position:relative;font-family:"Arimo",Arial,sans-serif;color:var(--white)}
  .abs{position:absolute}

  .topbar{left:0;top:0;width:1049px;height:50px;background:linear-gradient(var(--bar-mid),var(--bar-dark))}
  .subscribe{left:67px;top:17px;font:11px "Noto Sans",Verdana,sans-serif;color:#6e727c;letter-spacing:.3px}
  .subscribe a{color:#8a9bc0;text-decoration:none}
  .subscribe .sep{margin:0 6px;color:#555}
  .top-icon{top:16px;width:16px;height:16px;border-radius:3px}
  .search{left:791px;top:10px;width:184px;height:27px;border-radius:8px;background:#0d0e10;border:1px solid #2a2c30;font:10px "Noto Sans",Verdana,sans-serif;color:#4f535c;padding:7px 9px;letter-spacing:.5px}

  .scene{left:0;top:50px;width:1049px;height:878px;
    background:
      radial-gradient(ellipse 60% 30% at 50% 92%,rgba(70,70,90,.45),transparent 70%),
      linear-gradient(90deg,rgba(40,60,150,.35),transparent 12%,transparent 88%,rgba(40,60,150,.35)),
      linear-gradient(180deg,var(--sky-top) 0%,var(--sky-mid) 35%,#a9b3dc 55%,var(--sand) 75%,#b7b3c2 100%)}

  .logo{left:74px;top:64px;display:flex;flex-direction:column;align-items:flex-start;gap:6px}
  .logo-mark{width:44px;height:44px;border-radius:50%;background:var(--orange)}
  .logo-name{font-weight:700;font-size:13px;color:var(--orange)}

  .nav{left:440px;top:90px;width:528px;height:31px;border-radius:7px;background:linear-gradient(#7f97e8,#5a74d8)}
  .nav span{position:absolute;font-weight:700;font-size:17px;color:#eef1ff;top:6px;text-shadow:0 1px 1px rgba(0,0,40,.4)}

  .slider{left:63px;top:154px;width:912px;height:324px;
    background:
      linear-gradient(163deg,transparent 0%,transparent 44%,#e6e0cc 46%,#d6cfb8 49%,#6f9450 52%,#4d7a36 70%,#3b672a 100%),
      linear-gradient(180deg,#7da2c8 0%,#3f6f6a 7%,#2a6a98 10%,#1f74a4 40%,#2a8fb6 60%,#1f74a4 100%)}
  .dot{top:486px;width:14px;height:14px;border-radius:50%;background:#3a4466}
  .dot.on{background:#3ea0dc}

  .content{left:69px;top:519px;width:906px;height:390px;background:var(--panel)}
  .col-head{top:538px;height:44px;background:linear-gradient(var(--head-light),var(--head));display:flex;align-items:center;padding-left:46px;font-weight:700;font-size:20px}
  .col-head svg{position:absolute;left:12px;top:11px}
  .map{left:91px;top:581px;width:273px;height:224px;border:2px solid #cfd8e6;
    background:
      linear-gradient(125deg,transparent 55%,#cdb98a 56%,#c7b07c 75%,transparent 76%),
      linear-gradient(170deg,#b9c9cf 0%,#a9bcc4 50%,#6aa6d2 62%,#3e8fcc 100%)}
  .feed-img{left:403px;top:601px;width:238px;height:82px;
    background:
      linear-gradient(100deg,transparent 60%,#2f5a2c 62%,#4c6e3a 80%,#d9d4c4 100%),
      linear-gradient(180deg,#9fd8f0 0%,#6cc3e4 30%,#2fb9d8 55%,#48c9d8 75%,#ece6d6 92%)}
  .feed-title{left:403px;top:700px;width:238px;text-align:center;font-weight:700;font-size:17px}
  .btn{top:833px;height:38px;background:var(--btn);font-weight:700;font-size:12px;display:flex;align-items:center;justify-content:center}
  .comments{left:415px;top:845px;font-weight:700;font-size:12px}

  .touch{left:679px;top:582px;width:276px;height:222px;background:var(--touch)}
  .touch-item{left:703px;display:flex;align-items:flex-start;gap:10px;font-weight:700;font-size:13px}
  .touch-icon{width:29px;height:29px;border-radius:6px;display:flex;align-items:center;justify-content:center}
  .touch-item span{margin-top:1px}
  .social{left:679px;top:814px;width:276px;height:76px;background:var(--touch)}
  .soc{top:838px;width:29px;height:29px;border-radius:6px}

  .footer{left:0;top:928px;width:1049px;height:214px;background:var(--footer)}
  .f-head{top:957px;font-weight:700;font-size:21px;color:var(--footer-head)}
  .f-links{left:69px;top:1002px;list-style:none;font:12px "Noto Sans",Verdana,sans-serif;color:var(--footer-link);letter-spacing:.5px;line-height:19px}
  .thumb{width:51px;height:51px;background:#22263a;border:1px solid #2d3148;padding:4px}
  .thumb div{width:100%;height:100%}
  .bubble{left:680px;top:999px;width:291px;height:110px;border-radius:8px;background:var(--footer-box)}
  .bubble-tip{left:943px;top:982px}

  .bottombar{left:0;top:1142px;width:1049px;height:58px;background:#000}
  .copy{left:63px;top:1163px;font:11px "Noto Sans",Verdana,sans-serif;color:#1c1d22}
  .bottom-links{right:77px;top:1162px;font:11px "Noto Sans",Verdana,sans-serif;color:#7f8aa8;letter-spacing:.4px}
  .bottom-links .sep{margin:0 6px}
</style>
</head>
<body>
  <div class="abs topbar"></div>
  <div class="abs subscribe">Subscribe to: <a>Posts</a><span class="sep">|</span><a>Comments</a><span class="sep">|</span><a>Email</a></div>
  <div class="abs top-icon" style="left:714px;background:#e2761c"></div>
  <div class="abs top-icon" style="left:739px;background:#4b6bb0"></div>
  <div class="abs top-icon" style="left:764px;background:#5fb6d6"></div>
  <div class="abs search">Search Keywords</div>

  <div class="abs scene" role="img" aria-label="Soft-focus beach sand under a bright blue sky"></div>

  <div class="abs logo">
    <div class="logo-mark"></div>
    <div class="logo-name">Kestrel Shore Camp</div>
  </div>

  <nav class="abs nav">
    <span style="left:9px">Home</span>
    <span style="left:95px">Accommdation</span>
    <span style="left:237px">Activities</span>
    <span style="left:333px">Menu</span>
    <span style="left:402px">Private Camps</span>
  </nav>

  <div class="abs slider" role="img" aria-label="Aerial view of the camp setting: a long curved sandy beach, deep blue bay and green coastal farmland with the camp buildings by the dunes"></div>
  <div class="abs dot on" style="left:477px"></div>
  <div class="abs dot" style="left:496px"></div>
  <div class="abs dot" style="left:515px"></div>
  <div class="abs dot" style="left:534px"></div>
  <div class="abs dot" style="left:553px"></div>

  <div class="abs content"></div>

  <div class="abs col-head" style="left:90px;width:275px">
    <svg width="24" height="22" viewBox="0 0 24 22"><circle cx="12" cy="6" r="5" fill="#8e93a8"/><path d="M2 22c0-7 5-9 10-9s10 2 10 9z" fill="#8e93a8"/></svg>
    Location
  </div>
  <div class="abs col-head" style="left:384px;width:276px">
    <svg width="26" height="22" viewBox="0 0 26 22"><path d="M2 9c0-5 5-8 10-8s10 3 10 8-5 8-10 8l-6 4 1-5C4 15 2 12 2 9z" fill="#8e93a8"/></svg>
    FeedBack
  </div>
  <div class="abs col-head" style="left:679px;width:276px">
    <svg width="24" height="24" viewBox="0 0 24 24"><path d="M5 2l4 4-2 3c1 3 4 6 7 7l3-2 4 4-3 4C10 22 2 14 1 5z" fill="#8e93a8"/></svg>
    Get In Touch
  </div>

  <div class="abs map" role="img" aria-label="Locality map showing the roads from Melbourne to the camp on the bay, beside the national park"></div>
  <div class="abs feed-img" role="img" aria-label="Beach with palm trees and turquoise water"></div>
  <div class="abs feed-title">MY feedback</div>

  <div class="abs btn" style="left:110px;width:85px">Learn More</div>
  <div class="abs comments">23 Comments</div>
  <div class="abs btn" style="left:511px;width:83px">Read More</div>

  <div class="abs touch"></div>
  <div class="abs touch-item" style="top:605px">
    <div class="touch-icon" style="background:#3f86c9"><svg width="18" height="18" viewBox="0 0 24 24"><path d="M5 2l4 4-2 3c1 3 4 6 7 7l3-2 4 4-3 4C10 22 2 14 1 5z" fill="#fff"/></svg></div>
    <span>PHONE</span>
  </div>
  <div class="abs touch-item" style="top:654px">
    <div class="touch-icon" style="background:#e4e6ea"><svg width="22" height="16" viewBox="0 0 22 16"><rect x="1" y="1" width="20" height="14" fill="#f6f6f6" stroke="#aaa"/><path d="M1 1l10 8 10-8" fill="none" stroke="#aaa"/></svg></div>
    <span>EMAIL</span>
  </div>
  <div class="abs touch-item" style="top:703px">
    <div class="touch-icon"><svg width="29" height="29"><circle cx="14.5" cy="14.5" r="13" fill="#3fa9e0"/></svg></div>
    <span>CHATLINE</span>
  </div>
  <div class="abs touch-item" style="top:751px">
    <div class="touch-icon"><svg width="29" height="29"><circle cx="14.5" cy="14.5" r="13" fill="#3fa9e0"/></svg></div>
    <span>OTHER REQUEST</span>
  </div>

  <div class="abs social"></div>
  <div class="abs soc" style="left:703px;background:#5ec0dc"></div>
  <div class="abs soc" style="left:742px;background:#3c62ab"></div>
  <div class="abs soc" style="left:781px;background:#f0f0f4"></div>
  <div class="abs soc" style="left:820px;background:#2f86bf"></div>
  <div class="abs soc" style="left:859px;background:#3d5a7e"></div>
  <div class="abs soc" style="left:898px;background:#c3231f"></div>

  <footer class="abs footer"></footer>
  <div class="abs f-head" style="left:70px">About Us</div>
  <div class="abs f-head" style="left:215px">History</div>
  <div class="abs f-head" style="left:445px">The Gallery</div>
  <div class="abs f-head" style="left:694px">Updates</div>
  <ul class="abs f-links">
    <li>Our Company</li><li>Our Blog</li><li>Submit a Site</li><li>Contact Us</li><li>Help &amp; Terms</li><li>Read Our FAQ</li>
  </ul>

  <div class="abs thumb" style="left:395px;top:1003px"><div role="img" aria-label="Beach umbrella on sand" style="background:linear-gradient(#6cb8e8,#e7e0cf)"></div></div>
  <div class="abs thumb" style="left:456px;top:1003px"><div role="img" aria-label="Turquoise lagoon" style="background:linear-gradient(#5fb4da,#39c0c8)"></div></div>
  <div class="abs thumb" style="left:517px;top:1003px"><div role="img" aria-label="White sandy shore" style="background:linear-gradient(#8ad2e6,#f1f1ee)"></div></div>
  <div class="abs thumb" style="left:578px;top:1003px"><div role="img" aria-label="Rocky coastline" style="background:linear-gradient(#7fb2c4,#5b7c6a)"></div></div>
  <div class="abs thumb" style="left:395px;top:1062px"><div role="img" aria-label="Cliffs over a bay" style="background:linear-gradient(#5f8fb6,#2f6a7a)"></div></div>
  <div class="abs thumb" style="left:456px;top:1062px"><div role="img" aria-label="Resort by the sea" style="background:linear-gradient(#2e89c6,#3bb9d6)"></div></div>
  <div class="abs thumb" style="left:517px;top:1062px"><div role="img" aria-label="Palm tree over the beach" style="background:linear-gradient(#6cc5e2,#e7d9b2)"></div></div>
  <div class="abs thumb" style="left:578px;top:1062px"><div role="img" aria-label="Waves on the sand" style="background:linear-gradient(#9bd2e4,#f3f0e8)"></div></div>

  <svg class="abs bubble-tip" width="28" height="20" viewBox="0 0 28 20"><path d="M1 0v20h26z" fill="var(--footer-box)"/></svg>
  <div class="abs bubble"></div>

  <div class="abs bottombar"></div>
  <div class="abs copy">Copyright 2024 Kestrel Shore Camp. All rights reserved.</div>
  <div class="abs bottom-links">Log in<span class="sep">|</span>Privacy Policy<span class="sep">|</span>Terms and Conditions<span class="sep">|</span>Contact Us<span class="sep">|</span>Back to Top</div>
</body>
</html>
```